business card design - photography

I am a fine art photographer. I would like to approach galleries to exhibit my work and need a business card.

The card should convey creativity and simplicity.
I would like a double sided card.

Some options:
1. An all white card with raised or embossed text or design to create a tactile finish.
2. a white and dark grey design would also work well.
3. Would be great to use my name as part of the design but not essential.
4. My name and title on the front, other details on the back of card.

The final design should be simple, minimal, elegant and innovative.
Being minimal, it will be more about texture, text size and placement.

examples of designs I would prefer provided here:
http://plimvarka.com/ideas/40-quiet-and-refined-card-layouts

I'm also open to other designs that may be unusual and unique.

Love this:
http://www.snapvelo.com/pics/morningverselog/583014927
Updates

I have uploaded a psd file after playing around in photoshop with various fonts.  I like the font (which I downloaded from glyphmorra.com called Arual) but the design probably needs some refining.  I hope this helps.  If you'd like me to change the format of the file, please let me know.

Ilvane

Target Market(s)

Art Gallery owners/administrators and customers.

Industry/Entity Type

Business

Requirements
Must have
• A unique look.

Matte, silky finish or heavy textured stock. Double-sided card.

Front:
my name
photography by

Back:
phone no
email
web address
Nice to have
• Letterpress
embrossed
Clean fonts
Should not have
• Do not use illustrations of cameras or lenses.
No frames around the card edge.

```html
<!DOCTYPE html>
<html lang="en">
<head>
<meta charset="utf-8">
<title>Ilvane Merrow – Business Cards</title>
<link href="https://fonts.googleapis.com/css2?family=Caprasimo&family=Bitter:ital,wght@0,700;0,800;1,700&family=Cookie&display=swap" rel="stylesheet">
<style>
  :root {
    --backdrop: #d8d3ca;
    --teal-ink: #2a3538;
    --charcoal-ink: #242424;
    --cream: #ece6d8;
    --ornament: #b9b2a4;
  }
  * { box-sizing: border-box; margin: 0; padding: 0; }
  html, body { width: 1200px; height: 900px; overflow: hidden; }
  body { background: var(--backdrop); position: relative; font-family: "Bitter", Georgia, serif; }

  .card {
    position: absolute;
    top: 255px;
    width: 246px;
    height: 380px;
    background: var(--ink);
    box-shadow: 0 6px 14px rgba(0,0,0,0.25);
  }
  .card--teal { --ink: var(--teal-ink); }
  .card--charcoal { --ink: var(--charcoal-ink); }
  .pos-1 { left: 66px; }
  .pos-2 { left: 333px; }
  .pos-3 { left: 616px; }
  .pos-4 { left: 876px; }

  /* Front */
  .front-mark {
    position: absolute;
    left: 50%; top: 138px;
    transform: translateX(-50%);
    text-align: center;
  }
  .name-pill {
    display: inline-block;
    background: var(--cream);
    color: var(--ink);
    border-radius: 22px;
    padding: 9px 16px 8px;
    font-family: "Caprasimo", Georgia, serif;
    font-size: 23px;
    line-height: 0.95;
    text-transform: uppercase;
    letter-spacing: 0.5px;
  }
  .front-title {
    display: block;
    margin-top: 2px;
    color: var(--cream);
    font-family: "Cookie", cursive;
    font-size: 20px;
  }

  /* Back */
  .back-panel {
    position: absolute;
    inset: 9px;
    background: var(--cream);
    border-radius: 6px;
    padding: 5px;
  }
  .back-frame {
    height: 100%;
    border: 2px solid var(--ink);
    border-radius: 4px;
    display: flex;
    flex-direction: column;
    align-items: center;
    color: var(--ink);
    padding-top: 14px;
    overflow: hidden;
  }
  .seal-row { display: flex; align-items: center; gap: 10px; }
  .ornament { width: 34px; height: 10px; background: var(--ornament); border-radius: 5px; }
  .seal {
    width: 38px; height: 38px;
    border-radius: 50%;
    background: var(--ink);
    color: var(--cream);
    display: flex; align-items: center; justify-content: center;
    font-family: "Caprasimo", Georgia, serif;
    font-size: 15px;
  }
  .rule { width: 196px; border-top: 3px dotted var(--ink); margin: 10px 0 4px; }
  .headline {
    font-family: "Caprasimo", Georgia, serif;
    font-size: 27px;
    line-height: 1.1;
  }
  .headline--large { font-size: 31px; }
  .ink-pill {
    background: var(--ink);
    color: var(--cream);
    border-radius: 12px;
    width: 194px;
    text-align: center;
    font-family: "Caprasimo", Georgia, serif;
    font-style: italic;
    font-size: 20px;
    line-height: 28px;
    margin: 3px 0;
  }
  .contact-heading {
    font-family: "Bitter", Georgia, serif;
    font-weight: 800;
    font-size: 19px;
    letter-spacing: 0.3px;
    line-height: 1.1;
  }
  .contact-line {
    display: flex; align-items: center; gap: 4px;
    width: 196px;
    font-size: 9px; font-weight: 800;
    margin-top: 4px;
  }
  .contact-line .value { font-size: 9.5px; }
  .contact-line .value--pill {
    flex: 1;
    border: 2px solid var(--ink);
    border-radius: 10px;
    text-align: center;
    font-size: 14px;
    line-height: 16px;
    letter-spacing: 0.8px;
  }
  .web-band {
    margin-top: auto;
    width: 100%;
    background: var(--ink);
    color: var(--cream);
    text-align: center;
    padding: 6px 0 5px;
    font-size: 12px;
    font-weight: 800;
    line-height: 1;
  }
  .web-band small {
    display: block;
    font-family: "Bitter", Georgia, serif;
    font-style: italic;
    font-weight: 700;
    font-size: 7px;
    margin-top: 2px;
  }
</style>
</head>
<body>

  <section class="card card--teal pos-1" aria-label="Card front">
    <div class="front-mark">
      <span class="name-pill">Ilvane<br>Merrow</span>
      <span class="front-title">photographer</span>
    </div>
  </section>

  <section class="card card--teal pos-2" aria-label="Card back">
    <div class="back-panel">
      <div class="back-frame">
        <div class="seal-row">
          <span class="ornament" role="img" aria-label="scroll flourish"></span>
          <span class="seal">IM</span>
          <span class="ornament" role="img" aria-label="scroll flourish"></span>
        </div>
        <div class="rule"></div>
        <p class="headline">My Name is</p>
        <p class="ink-pill">Ilvane Merrow</p>
        <p class="headline headline--large">&amp; I'm a</p>
        <p class="ink-pill">Photographer</p>
        <div class="rule"></div>
        <p class="contact-heading">CONTACT ME</p>
        <p class="contact-line">phone: <span class="value value--pill">0491 207 384</span></p>
        <p class="contact-line">email: <span class="value">imerrow@postvela.com</span></p>
        <p class="web-band">www.ilvanemerrow.com<small>web address</small></p>
      </div>
    </div>
  </section>

  <section class="card card--charcoal pos-3" aria-label="Card front">
    <div class="front-mark">
      <span class="name-pill">Ilvane<br>Merrow</span>
      <span class="front-title">photographer</span>
    </div>
  </section>

  <section class="card card--charcoal pos-4" aria-label="Card back">
    <div class="back-panel">
      <div class="back-frame">
        <div class="seal-row">
          <span class="ornament" role="img" aria-label="scroll flourish"></span>
          <span class="seal">IM</span>
          <span class="ornament" role="img" aria-label="scroll flourish"></span>
        </div>
        <div class="rule"></div>
        <p class="headline">My Name is</p>
        <p class="ink-pill">Ilvane Merrow</p>
        <p class="headline headline--large">&amp; I'm a</p>
        <p class="ink-pill">Photographer</p>
        <div class="rule"></div>
        <p class="contact-heading">CONTACT ME</p>
        <p class="contact-line">phone: <span class="value value--pill">0491 207 384</span></p>
        <p class="contact-line">email: <span class="value">imerrow@postvela.com</span></p>
        <p class="web-band">www.ilvanemerrow.com<small>web address</small></p>
      </div>
    </div>
  </section>

</body>
</html>
```